Revamp a website that sells books on machine learning and A.I

Hello I would like to create a minimalist concept to revamp this website:

www.quillvane.co.uk

We can change everything including the logo.

Somethings that I don't like:
- Generic images of people.
- Robot images.

The books are about the mathematics for machine learning and A.I and I would like for the website to have a blog as well as a scheduling tool, were people can book a call with me.

The scheduling tool, needs to have text and different tiers, for example 15 m free and 60 m 45 usd

Target Market(s)

university students and mathematics enthusiasts

Industry/Entity Type

machine learning, education, books, mathematics, A.I

Number of Pages Required

4 page

Requirements
Must have
• Landing Page, blog page, scheduling page, optimised conversion funnel
Should not have
• Arbitrary images from people or robots

```html
<!DOCTYPE html>
<html lang="en">
<head>
<meta charset="utf-8">
<title>Quillvane — Beneath the Model</title>
<link href="https://fonts.googleapis.com/css2?family=Gelasio:wght@400;700&family=Roboto:wght@400;500;700&display=swap" rel="stylesheet">
<style>
:root{
  --stage:#1f1f1f;
  --page:#f7f8fc;
  --white:#ffffff;
  --orange:#f7a01b;
  --orange-dark:#e98c00;
  --brown:#8b4b0f;
  --ink:#2b2b2b;
  --muted:#8a8a8a;
  --peach:#fdeee6;
  --ribbon:#ffd08a;
  --red:#e23b2e;
  --line:#f1c9a0;
  --dots:#f2f3f8;
}
*{margin:0;padding:0;box-sizing:border-box}
html,body{width:1200px;height:2408px;overflow:hidden;background:var(--stage)}
h1,h2,h3,h4{font-weight:400}
.board{width:1284px;height:2576px;transform:scale(0.93458);transform-origin:0 0;position:relative;background:var(--stage);font-family:"Roboto",sans-serif;color:var(--ink)}
.page{position:absolute;top:15px;width:620px;background:var(--page);overflow:hidden}
.page--long{left:17px;height:2545px}
.page--short{left:647px;height:2415px}
.abs{position:absolute}

/* nav */
.nav{left:0;top:0;width:620px;height:38px;background:var(--white);box-shadow:0 2px 6px rgba(0,0,0,.08);z-index:3}
.brand{display:flex;align-items:center;gap:4px;font-family:"Gelasio",serif;font-weight:700;color:var(--orange);font-size:8px}
.brand i{width:9px;height:9px;border-radius:50%;background:var(--orange);display:block}
.nav-link{top:15px;font-size:5.5px;color:var(--ink)}
.nav-cart{left:515px;top:12px}
.nav-contact{left:551px;top:10px;width:54px;height:18px;border:1px solid var(--orange);border-radius:4px;color:var(--orange);font-size:5px;display:flex;align-items:center;justify-content:center}

/* hero */
.hero{left:0;top:38px;width:620px;height:365px;background:linear-gradient(90deg,#fdece2 0%,#fbf1ec 50%,#f6f7fb 100%)}
.kicker{font-size:7px;color:var(--orange);font-weight:500}
.hero-title{font-family:"Gelasio",serif;font-weight:700;color:var(--brown);font-size:17.5px;line-height:23px;white-space:nowrap}
.body-text{font-size:5.2px;line-height:10.6px;color:var(--ink)}
.quote-mark{font-family:"Gelasio",serif;color:var(--orange);font-size:16px;font-style:italic;line-height:1}
.quote{font-size:5.2px;line-height:10.6px;font-style:italic;color:var(--ink)}
.btn{background:var(--orange);color:var(--white);font-size:5px;font-weight:700;border-radius:3px;display:flex;align-items:center;justify-content:center;gap:5px;letter-spacing:.2px;box-shadow:0 3px 6px rgba(247,160,27,.3)}
.btn .book-ico{width:9px;height:6px;border-left:4px solid var(--white);border-right:4px solid var(--white);display:block}
.btn--big{font-size:5.5px;font-weight:700}
.art{border-radius:4px}

/* about */
.ribbon{background:var(--ribbon);clip-path:polygon(0 0,100% 0,100% 100%,50% 78%,0 100%)}
.about-name{font-family:"Gelasio",serif;font-weight:400;font-size:22px;color:var(--ink)}
.sub{font-size:6px;color:var(--muted)}
.social{width:18px;height:18px;border-radius:50%;background:var(--orange)}

/* reviews */
.reviews{left:0;width:620px;height:280px;background:radial-gradient(circle,#e6e8f0 1px,transparent 1.2px) 0 0/22px 22px,var(--dots)}
.section-title{font-family:"Gelasio",serif;font-weight:700;color:var(--brown);font-size:17px;width:620px;text-align:center}
.review{width:176px;height:102px;background:var(--white);border-radius:10px;box-shadow:0 3px 8px rgba(0,0,0,.08)}
.review b{position:absolute;left:42px;top:24px;font-size:6.5px;font-weight:700}
.review .quote-mark{position:absolute;left:22px;top:42px;font-size:14px}
.review p{position:absolute;left:42px;top:42px;width:118px;font-size:4.8px;line-height:6.6px;color:#555}

/* products */
.products{left:0;width:620px;background:var(--peach)}
.big-title{font-family:"Gelasio",serif;font-weight:400;font-size:22px;color:var(--ink);width:620px;text-align:center}
.product-card{background:var(--white);border-radius:10px}
.p-name{font-family:"Gelasio",serif;font-weight:700;font-size:7px;line-height:8.5px;color:var(--ink)}
.p-meta{font-size:4.8px;color:var(--muted)}
.p-price{font-size:10px;color:var(--ink)}
.cart-ico{width:7px;height:5px;border:1.4px solid var(--white);border-top:none;border-radius:0 0 1px 1px;display:block}

/* blog */
.blog-title{font-size:16px;font-weight:700;color:var(--orange)}
.blog-card{width:267px;height:97px;border-radius:10px;background:linear-gradient(90deg,#fdeee6,#fff6f1);box-shadow:0 3px 8px rgba(0,0,0,.08)}
.blog-card .art{position:absolute;left:26px;top:8px;width:86px;height:80px}
.blog-card h4{position:absolute;left:140px;top:17px;font-family:"Gelasio",serif;font-weight:700;font-size:7px;line-height:8px;color:var(--brown)}
.blog-card p{position:absolute;left:140px;top:40px;width:112px;font-size:4.8px;line-height:6.2px;color:#a48a7c}

/* tiers */
.tier-title{font-family:"Gelasio",serif;font-weight:700;color:var(--orange);font-size:18px;width:620px;text-align:center}
.tier-sub{font-size:5px;line-height:6.5px;color:var(--muted);width:620px;text-align:center}
.tier{width:181px;height:241px;background:var(--white);border-radius:10px;box-shadow:0 3px 10px rgba(0,0,0,.09);overflow:hidden}
.tier .corner{position:absolute;left:-28px;top:14px;width:110px;height:22px;background:var(--red);transform:rotate(-45deg);color:var(--white);font-size:9px;font-weight:700;display:flex;align-items:center;justify-content:center}
.tier h3{position:absolute;left:52px;top:22px;font-family:"Gelasio",serif;font-weight:700;font-size:10.5px;line-height:12px;color:var(--ink)}
.tier .desc{position:absolute;left:22px;top:60px;width:140px;font-size:4.8px;line-height:6.3px;color:var(--muted)}
.tier ul{position:absolute;left:22px;top:86px;list-style:none;width:140px}
.tier li{position:relative;padding-left:17px;font-size:4.8px;line-height:6.3px;color:var(--muted);margin-bottom:8px;min-height:13px}
.tier li::before{content:"";position:absolute;left:0;top:1px;width:10px;height:10px;border-radius:50%;background:var(--orange)}
.tier li::after{content:"";position:absolute;left:3px;top:3.5px;width:4px;height:2px;border-left:1.4px solid var(--white);border-bottom:1.4px solid var(--white);transform:rotate(-45deg)}
.tier .note{position:absolute;left:22px;top:164px;width:140px;font-size:4.8px;line-height:6.3px;color:var(--muted)}
.tier .btn{position:absolute;left:45px;top:197px;width:89px;height:31px}

/* contact */
.contact-title{font-family:"Gelasio",serif;font-weight:700;color:var(--orange);font-size:18px}
.contact-sub{font-size:5px;line-height:6.5px;color:var(--muted);width:270px}
.field{border:1px solid var(--line);border-radius:5px;background:var(--white);font-size:5px;color:var(--muted);padding:12px 13px}
.send{position:absolute;right:11px;bottom:11px;width:7px;height:5px;background:var(--orange);border-radius:1px}

/* footer */
.footer{left:0;width:620px}
.sub-title{font-size:7px;font-weight:500;color:var(--ink)}
.sub-field{width:146px;height:30px;border:1px solid var(--line);border-radius:4px;background:var(--white);font-size:5px;color:var(--muted);padding:12px 14px}
.sub-btn{position:absolute;right:-1px;top:-1px;width:31px;height:30px;background:var(--orange);border-radius:0 4px 4px 0}
.sub-btn::after{content:"";position:absolute;left:11px;top:12px;width:9px;height:6px;background:var(--white);border-radius:1px}
.rule{height:1px;background:#e4e4e4;width:540px;left:42px}
.copy{font-size:5px;color:var(--ink)}
.foot-link{font-size:5px;color:var(--ink)}
</style>
</head>
<body>
<div class="board">

<!-- ========== PAGE A ========== -->
<main class="page page--long">
  <header class="abs nav">
    <div class="abs brand" style="left:20px;top:14px"><i></i>Quillvane</div>
    <span class="abs nav-link" style="left:340px">Home</span>
    <span class="abs nav-link" style="left:383px">About</span>
    <span class="abs nav-link" style="left:428px">Books</span>
    <span class="abs nav-link" style="left:472px">Blogs</span>
    <svg class="abs nav-cart" width="13" height="12" viewBox="0 0 13 12"><path d="M0 1h2.5l2 7h6l1.5-5H3.5" fill="none" stroke="#f7a01b" stroke-width="1.6"/><circle cx="5" cy="10.5" r="1.2" fill="#f7a01b"/><circle cx="10" cy="10.5" r="1.2" fill="#f7a01b"/></svg>
    <span class="abs nav-contact">Contact Us</span>
  </header>

  <section class="abs hero">
    <div class="abs kicker" style="left:69px;top:71px">Latest Release</div>
    <h1 class="abs hero-title" style="left:69px;top:88px">Beneath the Model<br>Vol 2 - Calculus</h1>
    <svg class="abs" style="left:52px;top:108px" width="170" height="30" viewBox="0 0 170 30"><ellipse cx="83" cy="15" rx="82" ry="13" fill="none" stroke="#e98c00" stroke-width="1.2"/></svg>
    <p class="abs body-text" style="left:69px;top:154px;width:206px">Calculus is essential in machine learning and algorithm optimization, offering tools for function analysis and model tuning. Key concepts like derivatives and integrals are crucial for optimizing neural networks and minimizing error rates, making a strong understanding of calculus vital for success in these advanced fields.</p>
    <span class="abs quote-mark" style="left:69px;top:224px">“</span>
    <p class="abs quote" style="left:87px;top:219px;width:190px">Embark on a buzzing exploration of calculus in machine learning, where bees are your companions in deciphering the secrets of AI.</p>
    <p class="abs quote" style="left:87px;top:245px;font-size:4.8px;color:#888">— Tomas Varela</p>
    <a class="abs btn btn--big" style="left:69px;top:277px;width:114px;height:31px"><span class="book-ico"></span>START READING</a>
    <div class="abs art" role="img" aria-label="Book cover of Vol 2 Calculus with graduation cap and stacked books" style="left:358px;top:81px;width:212px;height:250px;background:linear-gradient(160deg,#f2c052 0%,#eab445 55%,#7d8a9c 85%,#3d4766 100%)"></div>
  </section>

  <div class="abs ribbon" style="left:69px;top:403px;width:85px;height:112px"></div>
  <div class="abs kicker" style="left:187px;top:434px">About Me</div>
  <h2 class="abs about-name" style="left:187px;top:454px">Tomas Varela</h2>
  <p class="abs sub" style="left:187px;top:493px">A Mathematician and now a book writer</p>
  <p class="abs body-text" style="left:187px;top:521px;width:196px">I am a mathematician with over a decade of experience in developing and deploying machine learning systems. My books are written in an conversational style with humour. They are rich in practical applications, enabling readers to not only grasp the concepts but also understand their real-world applications in the field of Data Science.</p>
  <div class="abs social" style="left:187px;top:597px"></div>
  <div class="abs art" role="img" aria-label="Open book illustration" style="left:428px;top:463px;width:180px;height:132px;background:radial-gradient(ellipse at 45% 45%,#f1f1f1 0%,#e3e3e3 40%,#d9a550 58%,transparent 62%)"></div>

  <section class="abs reviews" style="top:645px">
    <h2 class="abs section-title" style="top:60px">Customer's Reviews</h2>
    <article class="abs review" style="left:25px;top:106px"><b>Rowan</b><span class="quote-mark">“</span><p>As a student going into ML without much of a linear algebra foundation, I'm finding this book highly useful. Starts form the basics and works at a reasonable pace to establish core ML concepts...</p></article>
    <article class="abs review" style="left:222px;top:106px"><b>Callum Pryce</b><span class="quote-mark">“</span><p>...If you are looking for a resource that elegantly combines breadth and depth such you can understand the fundamentals of linear algebra to ultimately apply them to your ML projects, this is your stop...</p></article>
    <article class="abs review" style="left:418px;top:106px"><b style="top:20px">Ines</b><span class="quote-mark" style="top:38px">“</span><p style="top:38px">The conversational tone of the book is its biggest strength. It feels less like a traditional textbook and more like a novel. This approach makes the reader feel at ease, particularly when tackling complex topics</p></article>
  </section>

  <section class="abs products" style="top:927px;height:403px">
    <h2 class="abs big-title" style="top:45px">There are two of them!</h2>
    <div class="abs product-card" style="left:46px;top:168px;width:248px;height:132px">
      <div class="abs p-name" style="left:20px;top:18px">Beneath the Model Vol. 2 - Calculus</div>
      <div class="abs p-meta" style="left:20px;top:34px">EBOOK &nbsp;|&nbsp; PDF</div>
      <div class="abs p-price" style="left:20px;top:49px">$ 7.50</div>
      <a class="abs btn" style="left:31px;top:92px;width:114px;height:23px;font-size:6.5px"><span class="cart-ico"></span>Add to Cart</a>
    </div>
    <div class="abs art" role="img" aria-label="Covers of Vol 2 Calculus and Vol 1 Linear Algebra" style="left:343px;top:141px;width:180px;height:189px;background:linear-gradient(90deg,#efbd4f 0%,#e7b446 68%,#c9c9c9 70%,#b5b5b5 100%)"></div>
  </section>

  <h2 class="abs blog-title" style="left:56px;top:1370px">Latest Blog</h2>
  <a class="abs btn" style="left:184px;top:1365px;width:93px;height:31px"><span class="book-ico"></span>READ MORE</a>
  <article class="abs blog-card" style="left:56px;top:1434px"><div class="art" role="img" aria-label="Open book illustration" style="background:radial-gradient(ellipse,#eeeeee 0%,#dcdcdc 45%,#d9a550 62%,transparent 66%)"></div><h4>Beneath the Model<br>Vol. 2 - Calculus</h4><p>Lorem ipsum odor amet, consectetuer adipiscing elit. Velit commodo et phasellus per vitae torquent. Vehicula consequat ligula vehicula; facilisi tempus per venenatis suspendisse. Quisque dictumst tortor proin fusce id...</p></article>
  <article class="abs blog-card" style="left:338px;top:1434px"><div class="art" role="img" aria-label="Open book illustration" style="background:radial-gradient(ellipse,#eeeeee 0%,#dcdcdc 45%,#d9a550 62%,transparent 66%)"></div><h4>Beneath the Model<br>Vol. 2 - Calculus</h4><p>Lorem ipsum odor amet, consectetuer adipiscing elit. Velit commodo et phasellus per vitae torquent. Vehicula consequat ligula vehicula; facilisi tempus per venenatis suspendisse. Quisque dictumst tortor proin fusce id...</p></article>

  <h2 class="abs tier-title" style="top:1609px">Consultation Tiers</h2>
  <p class="abs tier-sub" style="top:1639px">Whether you're just beginning your journey or diving deeper into advanced topics, I offer personalized<br>consultations to fit your needs. Choose from the following options.</p>
  <article class="abs tier" style="left:109px;top:1691px">
    <span class="corner">FREE</span><h3>15-Minute<br>Consultation</h3>
    <p class="desc">Ideal for quick questions or initial discussions. Use this time to:</p>
    <ul><li>Clarify concepts in mathematics, machine learning, or AI.</li><li>Get insights on which of my books or resources might best fit your learning goals.</li><li>Explore how I can help guide your studies or projects.</li></ul>
    <p class="note">Perfect for brief, focused interactions with no cost!</p>
    <a class="btn"><span class="book-ico"></span>BOOK NOW</a>
  </article>
  <article class="abs tier" style="left:329px;top:1691px">
    <span class="corner">$45</span><h3>60-Minute Deep<br>Dive</h3>
    <p class="desc">A comprehensive session for those needing more in-depth guidance. During this paid consultation, we will:</p>
    <ul><li>Break down complex mathematical concepts essential to AI and machine learning.</li><li>Discuss specific problems you're facing in your studies or research.</li><li>Receive personalized advice on tackling mathematical challenges in AI projects.</li></ul>
    <p class="note">Best for students and professionals looking for a detailed, tailored approach to learning.</p>
    <a class="btn"><span class="book-ico"></span>BOOK NOW</a>
  </article>
  <div class="abs" role="img" aria-label="Blurred graduation cap decoration" style="left:240px;top:1795px;width:170px;height:140px;border-radius:50%;background:radial-gradient(ellipse,rgba(70,130,150,.55) 0%,rgba(90,150,170,.25) 50%,transparent 72%)"></div>

  <h2 class="abs contact-title" style="left:42px;top:2055px">Get in Touch</h2>
  <p class="abs contact-sub" style="left:42px;top:2084px">Have a question or want to know more about my books, blog, or consultations? Feel free to reach out to me directly.</p>
  <div class="abs field" style="left:42px;top:2128px;width:91px;height:29px">Name</div>
  <div class="abs field" style="left:142px;top:2128px;width:145px;height:29px">* Email</div>
  <div class="abs field" style="left:42px;top:2168px;width:245px;height:29px">Subject</div>
  <div class="abs field" style="left:42px;top:2208px;width:245px;height:69px">Message<span class="send"></span></div>
  <div class="abs art" role="img" aria-label="Alarm clock, pencil cup and calendar illustration" style="left:363px;top:2115px;width:220px;height:165px;background:radial-gradient(ellipse at 45% 55%,#f0b7c4 0%,#ebd6dc 40%,#eeeeee 60%,transparent 72%)"></div>

  <footer class="abs footer" style="top:2375px;height:170px;background:linear-gradient(180deg,#f7f8fc,#fbf6f3)">
    <div class="abs brand" style="left:53px;top:70px;font-size:9px"><i></i>Quillvane</div>
    <div class="abs sub-title" style="left:127px;top:51px">Subscribe for a &nbsp;free chapter!</div>
    <div class="abs sub-field" style="left:127px;top:71px">Email<span class="sub-btn"></span></div>
    <div class="abs social" style="left:567px;top:111px;width:12px;height:12px"></div>
    <div class="abs rule" style="top:134px"></div>
    <div class="abs copy" style="left:42px;top:147px">Copyright © 2023 All rights reserved by Quillvane</div>
    <span class="abs foot-link" style="left:413px;top:147px">Linear Algebra</span>
    <span class="abs foot-link" style="left:475px;top:147px">Calculus</span>
    <span class="abs foot-link" style="left:520px;top:147px">Probability &amp; Statistics</span>
  </footer>
</main>

<!-- ========== PAGE B ========== -->
<main class="page page--short">
  <header class="abs nav">
    <div class="abs brand" style="left:20px;top:14px"><i></i>Quillvane</div>
    <span class="abs nav-link" style="left:340px">Home</span>
    <span class="abs nav-link" style="left:383px">About</span>
    <span class="abs nav-link" style="left:428px">Books</span>
    <span class="abs nav-link" style="left:472px">Blogs</span>
    <svg class="abs nav-cart" width="13" height="12" viewBox="0 0 13 12"><path d="M0 1h2.5l2 7h6l1.5-5H3.5" fill="none" stroke="#f7a01b" stroke-width="1.6"/><circle cx="5" cy="10.5" r="1.2" fill="#f7a01b"/><circle cx="10" cy="10.5" r="1.2" fill="#f7a01b"/></svg>
    <span class="abs nav-contact">Contact Us</span>
  </header>

  <section class="abs hero">
    <div class="abs kicker" style="left:69px;top:67px">Latest Release</div>
    <h1 class="abs hero-title" style="left:69px;top:88px">Beneath the Model<br>Vol 2 - Calculus</h1>
    <div class="abs" style="left:69px;top:131px;width:140px;height:1.4px;background:var(--brown)"></div>
    <p class="abs body-text" style="left:69px;top:154px;width:206px">Calculus is essential in machine learning and algorithm optimization, offering tools for function analysis and model tuning. Key concepts like derivatives and integrals are crucial for optimizing neural networks and minimizing error rates, making a strong understanding of calculus vital for success in these advanced fields.</p>
    <span class="abs quote-mark" style="left:69px;top:224px">“</span>
    <p class="abs quote" style="left:87px;top:219px;width:190px">Embark on a buzzing exploration of calculus in machine learning, where bees are your companions in deciphering the secrets of AI.</p>
    <p class="abs quote" style="left:87px;top:245px;font-size:4.8px;color:#888">— Tomas Varela</p>
    <a class="abs btn btn--big" style="left:69px;top:277px;width:114px;height:31px"><span class="book-ico"></span>START READING</a>
    <div class="abs art" role="img" aria-label="Graduation cap on stacked books beside the Vol 2 Calculus cover" style="left:323px;top:81px;width:255px;height:250px;background:linear-gradient(200deg,#f2c052 0%,#eab445 55%,#7d8a9c 85%,#3d4766 100%)"></div>
  </section>

  <div class="abs ribbon" style="left:69px;top:403px;width:85px;height:112px"></div>
  <div class="abs kicker" style="left:187px;top:434px">About Me</div>
  <h2 class="abs about-name" style="left:187px;top:454px">Tomas Varela</h2>
  <p class="abs sub" style="left:187px;top:493px">A Mathematician and now a book writer</p>
  <p class="abs body-text" style="left:187px;top:521px;width:196px">I am a mathematician with over a decade of experience in developing and deploying machine learning systems. My books are written in an conversational style with humour. They are rich in practical applications, enabling readers to not only grasp the concepts but also understand their real-world applications in the field of Data Science.</p>
  <div class="abs social" style="left:187px;top:597px"></div>
  <div class="abs art" role="img" aria-label="Open book illustration" style="left:428px;top:463px;width:180px;height:132px;background:radial-gradient(ellipse at 45% 45%,#f1f1f1 0%,#e3e3e3 40%,#d9a550 58%,transparent 62%)"></div>

  <section class="abs reviews" style="top:645px">
    <h2 class="abs section-title" style="top:60px">Customer's Reviews</h2>
    <article class="abs review" style="left:25px;top:106px"><b>Rowan</b><span class="quote-mark">“</span><p>As a student going into ML without much of a linear algebra foundation, I'm finding this book highly useful. Starts form the basics and works at a reasonable pace to establish core ML concepts...</p></article>
    <article class="abs review" style="left:222px;top:106px"><b>Callum Pryce</b><span class="quote-mark">“</span><p>...If you are looking for a resource that elegantly combines breadth and depth such you can understand the fundamentals of linear algebra to ultimately apply them to your ML projects, this is your stop...</p></article>
    <article class="abs review" style="left:418px;top:106px"><b style="top:20px">Ines</b><span class="quote-mark" style="top:38px">“</span><p style="top:38px">The conversational tone of the book is its biggest strength. It feels less like a traditional textbook and more like a novel. This approach makes the reader feel at ease, particularly when tackling complex topics</p></article>
  </section>

  <section class="abs products" style="top:927px;height:270px">
    <h2 class="abs big-title" style="top:45px">There are two of them!</h2>
    <div class="abs art" role="img" aria-label="Cover of Vol 2 Calculus" style="left:43px;top:130px;width:60px;height:94px;background:linear-gradient(180deg,#f2c052,#e3ad3f)"></div>
    <div class="abs p-name" style="left:137px;top:134px">Beneath the Model<br>Vol. 2 - Calculus</div>
    <div class="abs p-meta" style="left:137px;top:156px">EBOOK &nbsp;|&nbsp; PDF</div>
    <div class="abs p-price" style="left:137px;top:171px">$ 7.50</div>
    <a class="abs btn" style="left:137px;top:203px;width:114px;height:23px;font-size:6.5px"><span class="cart-ico"></span>Add to Cart</a>
    <div class="abs art" role="img" aria-label="Cover of Vol 1 Linear Algebra" style="left:348px;top:130px;width:62px;height:94px;background:linear-gradient(180deg,#f2c052,#e3a33a)"></div>
    <div class="abs p-name" style="left:439px;top:134px">Beneath the Model<br>Vol. 2 - Calculus</div>
    <div class="abs p-meta" style="left:439px;top:156px">EBOOK &nbsp;|&nbsp; PDF</div>
    <div class="abs p-price" style="left:439px;top:171px">$ 7.50</div>
    <a class="abs btn" style="left:439px;top:203px;width:114px;height:23px;font-size:6.5px"><span class="cart-ico"></span>Add to Cart</a>
  </section>

  <h2 class="abs blog-title" style="left:56px;top:1239px">Latest Blog</h2>
  <a class="abs btn" style="left:184px;top:1234px;width:93px;height:31px"><span class="book-ico"></span>READ MORE</a>
  <article class="abs blog-card" style="left:56px;top:1303px"><div class="art" role="img" aria-label="Open book illustration" style="background:radial-gradient(ellipse,#eeeeee 0%,#dcdcdc 45%,#d9a550 62%,transparent 66%)"></div><h4>Beneath the Model<br>Vol. 2 - Calculus</h4><p>Lorem ipsum odor amet, consectetuer adipiscing elit. Velit commodo et phasellus per vitae torquent. Vehicula consequat ligula vehicula; facilisi tempus per venenatis suspendisse. Quisque dictumst tortor proin fusce id...</p></article>
  <article class="abs blog-card" style="left:338px;top:1303px"><div class="art" role="img" aria-label="Open book illustration" style="background:radial-gradient(ellipse,#eeeeee 0%,#dcdcdc 45%,#d9a550 62%,transparent 66%)"></div><h4>Beneath the Model<br>Vol. 2 - Calculus</h4><p>Lorem ipsum odor amet, consectetuer adipiscing elit. Velit commodo et phasellus per vitae torquent. Vehicula consequat ligula vehicula; facilisi tempus per venenatis suspendisse. Quisque dictumst tortor proin fusce id...</p></article>

  <div class="abs" role="img" aria-label="Graduation cap decoration" style="left:480px;top:1455px;width:150px;height:140px;border-radius:50%;background:radial-gradient(ellipse,rgba(70,130,150,.85) 0%,rgba(90,150,170,.4) 50%,transparent 72%)"></div>
  <div class="abs" role="img" aria-label="Blurred graduation cap decoration" style="left:0;top:1600px;width:120px;height:100px;border-radius:50%;background:radial-gradient(ellipse,rgba(70,130,150,.5) 0%,rgba(90,150,170,.2) 50%,transparent 72%)"></div>
  <h2 class="abs tier-title" style="top:1478px">Consultation Tiers</h2>
  <p class="abs tier-sub" style="top:1508px">Whether you're just beginning your journey or diving deeper into advanced topics, I offer personalized<br>consultations to fit your needs. Choose from the following options.</p>
  <article class="abs tier" style="left:110px;top:1560px">
    <span class="corner">FREE</span><h3>15-Minute<br>Consultation</h3>
    <p class="desc">Ideal for quick questions or initial discussions. Use this time to:</p>
    <ul><li>Clarify concepts in mathematics, machine learning, or AI.</li><li>Get insights on which of my books or resources might best fit your learning goals.</li><li>Explore how I can help guide your studies or projects.</li></ul>
    <p class="note">Perfect for brief, focused interactions with no cost!</p>
    <a class="btn"><span class="book-ico"></span>BOOK NOW</a>
  </article>
  <article class="abs tier" style="left:329px;top:1560px">
    <span class="corner">$45</span><h3>60-Minute Deep<br>Dive</h3>
    <p class="desc">A comprehensive session for those needing more in-depth guidance. During this paid consultation, we will:</p>
    <ul><li>Break down complex mathematical concepts essential to AI and machine learning.</li><li>Discuss specific problems you're facing in your studies or research.</li><li>Receive personalized advice on tackling mathematical challenges in AI projects.</li></ul>
    <p class="note">Best for students and professionals looking for a detailed, tailored approach to learning.</p>
    <a class="btn"><span class="book-ico"></span>BOOK NOW</a>
  </article>

  <h2 class="abs contact-title" style="left:42px;top:1923px">Get in Touch</h2>
  <p class="abs contact-sub" style="left:42px;top:1952px">Have a question or want to know more about my books, blog, or consultations? Feel free to reach out to me directly.</p>
  <div class="abs field" style="left:42px;top:1997px;width:91px;height:29px">Name</div>
  <div class="abs field" style="left:142px;top:1997px;width:145px;height:29px">* Email</div>
  <div class="abs field" style="left:42px;top:2037px;width:245px;height:29px">Subject</div>
  <div class="abs field" style="left:42px;top:2077px;width:245px;height:69px">Message<span class="send"></span></div>
  <div class="abs art" role="img" aria-label="Alarm clock, pencil cup and calendar illustration" style="left:363px;top:1985px;width:200px;height:165px;background:radial-gradient(ellipse at 45% 55%,#f0b7c4 0%,#ebd6dc 40%,#eeeeee 60%,transparent 72%)"></div>

  <footer class="abs footer" style="top:2247px;height:168px;background:linear-gradient(90deg,#f7f8fc,#fdeee6)">
    <div class="abs brand" style="left:53px;top:48px;font-size:9px"><i></i>Quillvane</div>
    <div class="abs sub-title" style="left:127px;top:46px">Subscribe for a &nbsp;free chapter!</div>
    <div class="abs sub-field" style="left:127px;top:68px">Email<span class="sub-btn"></span></div>
    <div class="abs social" style="left:567px;top:108px;width:12px;height:12px"></div>
    <div class="abs copy" style="left:42px;top:144px">Copyright © 2023 All rights reserved by Quillvane</div>
    <span class="abs foot-link" style="left:413px;top:144px">Linear Algebra</span>
    <span class="abs foot-link" style="left:475px;top:144px">Calculus</span>
    <span class="abs foot-link" style="left:520px;top:144px">Probability &amp; Statistics</span>
  </footer>
</main>

</div>
</body>
</html>
```